Design a cover for a book called The Quiet Harvest

Describe a cover for a 5.5" x 8.5" 200-page paperback book titled The Quiet Harvest. The subtitle is: A Civic Field Manual for Shaping a Country Where Families Can Thrive Together

The book is about how we can change our economic system to provide universal basic income, free healthcare, and free college while also lowering our tax rates. The book is uplifting, talks about the spiritual growth our society will need in positive terms. The website TheCommonLedgerPlan.example will be used to promote the book, and is a good resources for design ideas.

Target Market(s)

Economics, Finance, Spiritual

Font styles to use
Serif
Sans Serif

Colors

Designer to choose colors to be used in the design.

Requirements
Must have
• Include the URL on the back cover: TheQuietHarvest.example
Include the attached ISBN Barcode on the back cover
Include the title on the front cover: The Quiet Harvest
Include the subtitle on the front cover: A Civic Field Manual for Shaping a Country Where Families Can Thrive Together
Include the author's name Martin Lowell Perry on the front cover

Here is the size of the cover:
Spine Width 0.4504” (200 x 0.002252”)
Full Width 11.7004” (0.125 + 5.5 + 0.4504 + 5.5 +0.125) 3511 pixels @300DPI
Full Height 8.75” (0.125 + 8.5 + 0.125) 2625 pixels @ 300DPI

```html
<!DOCTYPE html>
<html lang="en">
<head>
<meta charset="utf-8">
<title>The Quiet Harvest — Front Cover</title>
<link href="https://fonts.googleapis.com/css2?family=Saira+Extra+Condensed:wght@400;500;600&display=swap" rel="stylesheet">
<style>
  :root {
    --page-bg: #e7e3dc;
    --cover-black: #050505;
    --title-white: #ffffff;
    --title-gold: #a2813c;
    --rule-gold: #8a6d33;
    --rule-grey: #d9d9d9;
    --scene-gold: #6e5626;
    --scene-green: #3d4a2a;
    --scene-rust: #4a2a16;
  }
  html, body {
    margin: 0;
    padding: 0;
    width: 1200px;
    height: 1000px;
    overflow: hidden;
    background: var(--page-bg);
  }
  .canvas {
    position: relative;
    width: 1200px;
    height: 1000px;
  }
  .front-cover {
    position: absolute;
    left: 284px;
    top: 27px;
    width: 632px;
    height: 945px;
    background: var(--cover-black);
    overflow: hidden;
    box-shadow: 0 6px 24px rgba(0,0,0,0.25);
  }
  .cover-art {
    position: absolute;
    left: 0;
    top: 480px;
    width: 632px;
    height: 410px;
    background:
      radial-gradient(ellipse 55% 45% at 45% 45%, rgba(160,150,80,0.55), transparent 70%),
      radial-gradient(ellipse 40% 50% at 80% 30%, rgba(110,60,25,0.6), transparent 70%),
      radial-gradient(ellipse 35% 40% at 20% 75%, rgba(61,74,42,0.7), transparent 70%),
      linear-gradient(180deg, var(--cover-black) 0%, var(--scene-rust) 30%, var(--scene-gold) 55%, var(--scene-green) 75%, var(--cover-black) 100%);
  }
  .cover-type {
    position: absolute;
    left: 0;
    top: 0;
    width: 632px;
    height: 945px;
    font-family: "Saira Extra Condensed", "Arial Narrow", sans-serif;
  }
  .series-word { fill: var(--title-gold); font-weight: 500; font-size: 86px; }
  .title-white { fill: var(--title-white); font-weight: 500; font-size: 150px; }
  .title-gold { fill: var(--title-gold); font-weight: 500; font-size: 157px; }
  .subtitle { fill: var(--title-white); font-weight: 400; font-size: 26px; }
  .author { fill: var(--title-white); font-weight: 500; font-size: 78px; }
  .rule-grey { stroke: var(--rule-grey); stroke-width: 2; }
  .rule-gold { stroke: var(--rule-gold); stroke-width: 1.5; }
</style>
</head>
<body>
<main class="canvas">
  <section class="front-cover">
    <div class="cover-art" role="img" aria-label="Night photograph of an illuminated bridge over a river under a dark amber sky"></div>
    <svg class="cover-type" viewBox="0 0 632 945" xmlns="http://www.w3.org/2000/svg" aria-label="The Quiet Harvest, by Martin Lowell Perry">
      <line class="rule-grey" x1="130" y1="90" x2="247" y2="90"/>
      <line class="rule-grey" x1="387" y1="90" x2="525" y2="90"/>
      <text class="series-word" x="317" y="120" text-anchor="middle" textLength="68" lengthAdjust="spacingAndGlyphs">THE</text>
      <text class="title-white" x="328" y="245" text-anchor="middle" textLength="397" lengthAdjust="spacingAndGlyphs">QUIET</text>
      <text class="title-gold" x="328" y="375" text-anchor="middle" textLength="397" lengthAdjust="spacingAndGlyphs">HARVEST</text>
      <line class="rule-gold" x1="130" y1="400" x2="527" y2="400"/>
      <text class="subtitle" x="328" y="446" text-anchor="middle" textLength="398" lengthAdjust="spacingAndGlyphs">A CIVIC FIELD MANUAL FOR SHAPING A COUNTRY</text>
      <text class="subtitle" x="328" y="474" text-anchor="middle" textLength="300" lengthAdjust="spacingAndGlyphs">WHERE FAMILIES CAN THRIVE TOGETHER</text>
      <text class="author" x="321" y="910" text-anchor="middle" textLength="528" lengthAdjust="spacingAndGlyphs">MARTIN LOWELL PERRY</text>
    </svg>
  </section>
</main>
</body>
</html>
```